Logo and Double sided business card

We need a logo and business card for a Point of Sale Business, Website is www.tillcrest.com.au - this is being worked on at the moment. There is a logo on the website - but this is more of a placement /logo and needs to be redesigned.
The address for Details for the Business card are

Person Name
TILL CREST
27/3 Worrin St
Brenmoor Vale 2163
Ph 1300 482 519 (1300 TIL 519)
Email : Person@tillcrest.com.au
Web: www.tillcrest.com.au

Our company will be a Point of Sale installation and Support business. We Specialise in the Quandel Tivra system.

We do
Installation of POS Systems
Support and Maintenance of existing POS
Tivra POS support
Updates

Target Market(s)

Restaurants, hotels, retail shops

Industry/Entity Type

Business

Contact Information for Business Card

Person Name
TILL CREST
27/3 Worrin St
Brenmoor Vale 2163
Web: www.tillcrest.com.au

Logo Text

Till Crest

Font styles to use
Serif

Requirements
Must have
• We must have the source graphics in editable formats for both logo and business card.

```html
<!DOCTYPE html>
<html lang="en">
<head>
<meta charset="utf-8">
<title>Till Crest – Business Card</title>
<link rel="stylesheet" href="https://fonts.googleapis.com/css2?family=Montserrat:wght@400;500;700;800&display=swap">
<style>
  :root {
    --bg: #e9e7e4;
    --card-white: #ffffff;
    --ink: #1a1a1a;
    --ink-soft: #3d3d3d;
    --brand-yellow: #fcc21b;
    --brand-black: #111111;
    --text-light: #ffffff;
  }
  * { box-sizing: border-box; margin: 0; padding: 0; }
  html, body { width: 1200px; height: 1000px; overflow: hidden; }
  body {
    background: var(--bg);
    font-family: "Montserrat", Arial, sans-serif;
    position: relative;
  }
  .card {
    position: absolute;
    width: 560px;
    height: 320px;
    box-shadow: 0 6px 18px rgba(0,0,0,0.18);
    overflow: hidden;
  }
  /* Front */
  .card-front { left: 90px; top: 120px; background: var(--card-white); }
  .front-brand {
    position: absolute; left: 40px; top: 118px;
    display: flex; align-items: center; gap: 10px;
  }
  .brand-square { width: 22px; height: 22px; background: var(--brand-yellow); }
  .brand-name {
    font-weight: 800; font-size: 24px; letter-spacing: 0.5px; color: var(--ink);
    white-space: nowrap;
  }
  .divider {
    position: absolute; left: 246px; top: 70px; width: 2px; height: 110px;
    background: var(--brand-yellow);
  }
  .contact { position: absolute; left: 272px; top: 68px; color: var(--ink-soft); white-space: nowrap; }
  .contact .person { font-weight: 700; font-size: 22px; color: var(--ink); margin-bottom: 8px; }
  .contact .role { font-weight: 500; font-size: 15px; color: var(--ink-soft); }
  .contact .line { font-size: 13.5px; line-height: 17px; }
  .contact .gap { margin-top: 6px; }
  .services {
    position: absolute; left: 0; right: 0; bottom: 24px; height: 62px;
    display: flex;
  }
  .service {
    flex: 1; position: relative;
    display: flex; align-items: center; justify-content: center; text-align: center;
    font-size: 13px; font-weight: 500; line-height: 16px; padding: 0 14px;
    background: var(--brand-black); color: var(--text-light);
  }
  .service::before {
    content: ""; position: absolute; top: -7px; left: 50%; transform: translateX(-50%);
    border-left: 8px solid transparent; border-right: 8px solid transparent;
    border-bottom: 8px solid var(--brand-black);
  }
  .service.highlight { background: var(--brand-yellow); color: var(--brand-black); }
  .service.highlight::before { border-bottom-color: var(--brand-yellow); }
  /* Back */
  .card-back {
    left: 550px; top: 540px; background: var(--brand-black);
    display: flex; align-items: center; justify-content: center; gap: 22px;
  }
  .card-back .brand-square { width: 40px; height: 40px; }
  .back-rule { width: 2px; height: 70px; background: var(--text-light); }
  .card-back .brand-name { font-size: 40px; color: var(--brand-yellow); line-height: 1; }
</style>
</head>
<body>
  <section class="card card-front" aria-label="Business card front">
    <div class="front-brand">
      <span class="brand-square"></span>
      <span class="brand-name">TILL CREST</span>
    </div>
    <div class="divider"></div>
    <div class="contact">
      <p class="person">John Doe</p>
      <p class="role">IE Sales</p>
      <p class="line">1300 482 519 (1300 TIL 519)</p>
      <p class="line gap">Person@tillcrest.com.au</p>
      <p class="line">www.tillcrest.com.au</p>
      <p class="line">27/3 Worrin St, Brenmoor Vale 2163</p>
    </div>
    <div class="services">
      <div class="service">Installation of POS<br>Systems</div>
      <div class="service highlight">Tivra POS support</div>
      <div class="service">Maintenance of<br>existing POS</div>
    </div>
  </section>

  <section class="card card-back" aria-label="Business card back">
    <span class="brand-square"></span>
    <span class="back-rule"></span>
    <span class="brand-name">TILL CREST</span>
  </section>
</body>
</html>
```